Brightway Dwelling & Yard Care - Maintenance & Improvements

Handyman service - Total home improvement and maintenance

We do everything indoors, ie. carpentry, and outdoors, ie. garden maintenance

No job too small or too unusual

7 Days per week
Updates

I want the overall impression not to favour either gender ... eg. maybe don't use the word Handy'man' because we also have a Fixmistress service .... but just stay with a generic theme of home improvement and maintenance

Industry/Entity Type

Home Improvement

Contact Information for Business Card

Brightway Dwelling & Yard Care
7 Days per Week
Total Home Maintenance and Improvements
Handyman | Fixmistress | Our (DIY) Task Pal
Ph: 0487 613 902
www.brightwaydwellingyard.com.au

Requirements
Must have
• The black and white image of various workers, as per attached

```html
<!DOCTYPE html>
<html lang="en">
<head>
<meta charset="utf-8">
<title>Brightway Dwelling &amp; Yard Care – Business Card</title>
<link rel="stylesheet" href="https://fonts.googleapis.com/css2?family=Open+Sans:wght@400;600;700&display=swap">
<style>
  :root {
    --page-bg: #ffffff;
    --card-bg: #f2f2f2;
    --card-edge: #c9c9c9;
    --ink: #111111;
    --ink-soft: #1e1e1e;
    --photo-leaf: #3f7a3a;
    --photo-wood: #b36a2c;
    --photo-sky: #7fa7c2;
    --worker-shade: #d8d8d8;
    --worker-shade-top: #e6e6e6;
  }
  * { box-sizing: border-box; margin: 0; padding: 0; }
  html, body {
    width: 1200px;
    height: 823px;
    overflow: hidden;
    background: var(--page-bg);
    font-family: "Open Sans", sans-serif;
    color: var(--ink);
  }
  .business-card {
    position: absolute;
    left: 80px;
    top: 73px;
    width: 1040px;
    height: 676px;
    background: var(--card-bg);
    border: 1.5px solid var(--card-edge);
    border-radius: 28px;
    overflow: hidden;
  }
  .workers-band {
    position: absolute;
    left: 0;
    bottom: 0;
    width: 100%;
    height: 150px;
    background: linear-gradient(to bottom, var(--worker-shade-top) 0%, var(--worker-shade) 35%, var(--worker-shade) 100%);
  }
  .feature-photo {
    position: absolute;
    left: 27px;
    top: 30px;
    width: 240px;
    height: 267px;
    border: 1.5px solid var(--ink);
    background: linear-gradient(to bottom, var(--photo-leaf) 0%, #5d8a4a 30%, var(--photo-wood) 55%, #c9b49a 72%, var(--photo-sky) 100%);
  }
  .brand {
    position: absolute;
    left: 266px;
    top: 0;
  }
  .brand-lead {
    position: absolute;
    left: 28px;
    top: 62px;
    font-size: 35px;
    font-weight: 700;
    white-space: nowrap;
  }
  .brand-name {
    position: absolute;
    left: 26px;
    top: 108px;
    font-size: 59px;
    font-weight: 400;
    white-space: nowrap;
    letter-spacing: 0.3px;
  }
  .tagline {
    position: absolute;
    left: 28px;
    top: 190px;
    font-size: 29px;
    line-height: 36px;
    color: var(--ink-soft);
    white-space: nowrap;
  }
  .service-name {
    position: absolute;
    left: 26px;
    top: 408px;
    font-size: 37px;
    font-weight: 700;
  }
  .service-line {
    position: absolute;
    left: 26px;
    top: 458px;
    font-size: 28px;
    color: var(--ink-soft);
  }
  .contact-list {
    position: absolute;
    left: 26px;
    top: 520px;
    list-style: none;
  }
  .contact-item {
    display: flex;
    align-items: center;
    height: 40px;
    font-size: 28px;
  }
  .contact-icon {
    width: 24px;
    height: 24px;
    margin-right: 24px;
    flex: none;
  }
</style>
</head>
<body>
  <article class="business-card">
    <div class="workers-band" role="img" aria-label="Black and white silhouettes of various workers: painter, ladder, gardener, mower and plumber"></div>

    <div class="feature-photo" role="img" aria-label="Photo of a garden pergola with wicker outdoor sofas and orange cushions"></div>

    <header class="brand">
      <p class="brand-lead">Brightway</p>
      <h1 class="brand-name">Dwelling &amp; Yard Care</h1>
      <p class="tagline">7 Days per Week Total Home Maintenance<br>Improvements Handyman</p>
    </header>

    <h2 class="service-name">Fixmistress</h2>
    <p class="service-line">Our (DIY) Task Pal</p>

    <ul class="contact-list">
      <li class="contact-item">
        <svg class="contact-icon" viewBox="0 0 24 24" aria-hidden="true">
          <path d="M3 9c0-3 4-5 9-5s9 2 9 5v2h-5V9c-1-.7-2.5-1-4-1s-3 .3-4 1v2H3z" fill="#111"/>
          <path d="M6 12h12l2 8H4z" fill="#111"/>
          <circle cx="12" cy="16" r="2.4" fill="#f2f2f2"/>
        </svg>
        <span>0487 613 902</span>
      </li>
      <li class="contact-item">
        <svg class="contact-icon" viewBox="0 0 24 24" aria-hidden="true">
          <g fill="none" stroke="#111" stroke-width="1.8">
            <circle cx="12" cy="12" r="10"/>
            <ellipse cx="12" cy="12" rx="4.5" ry="10"/>
            <line x1="2" y1="12" x2="22" y2="12"/>
            <path d="M4 7h16M4 17h16"/>
          </g>
        </svg>
        <span>www.brightwaydwellingyard.com.au</span>
      </li>
    </ul>
  </article>
</body>
</html>
```